Letterhead for New Orthopaedic Surgery Practice

My husband and I are starting our own practice named RB Spine & Vitality Center. We would like to create a nice simple but high class letterhead that doesn't use too much solid color ink when printing. I like the colors dark blue, gold, yellow. Open to other suggestions. We will need to list him and I both on the top of the letterhead. Here is the important information:
Lucinda Perrow, M.D. - Hand and Upper Extremity Surgery
Abena Quist, M.D. - Hip & Knee Replacement/General Orthopaedic Surgery
Location: 18735 North Harlow Pkwy
Maple Grove, FL 33418
Phone: 954-218-4650
Fax: 954-582-1346
Email: info@myrbspine.com

The only thing is that the phone and fax numbers will change once we get into our space. I just want to get the design started. I am including several documents which are my previous practice letterhead, my current procedure room letterhead, and our new Logo. The other letterheads are just for examples but please think outside of the box! We would love to see some great designs.

Colors
0054AA
0677BA
7BADD7
CADEEF
E8F1F8
0094D4
00A9DD
6FCCEA
C7EBF8
E9F6FB

Requirements
Must have
• class, elegance, luxury

```html
<!DOCTYPE html>
<html lang="en">
<head>
<meta charset="utf-8">
<title>RB Spine &amp; Vitality Center — Letterhead</title>
<link rel="stylesheet" href="https://fonts.googleapis.com/css2?family=Tinos:wght@400;700&display=swap">
<style>
  :root {
    --navy: #1b284e;
    --gold: #c5a25e;
    --ink: #2a2a2a;
    --rule: #6b6b6b;
    --watermark: #dcdee5;
    --backdrop: #e9e8e7;
    --paper: #ffffff;
  }
  * { margin: 0; padding: 0; box-sizing: border-box; }
  html, body {
    width: 1200px; height: 1200px; overflow: hidden;
    background: var(--backdrop);
    font-family: "Tinos", "Times New Roman", serif;
  }
  .letterhead {
    position: absolute; left: 176px; top: 0;
    width: 848px; height: 1200px;
    background: var(--paper);
    overflow: hidden;
  }
  .brand-mark {
    position: absolute; left: 52px; top: 44px;
    width: 130px; height: 130px;
    border: 2px solid var(--gold); border-radius: 50%;
    display: flex; align-items: center; justify-content: center;
    text-align: center;
    color: var(--navy); font-weight: 700; font-size: 15px; line-height: 1.2;
    padding: 0 14px;
  }
  .physicians {
    position: absolute; right: 248px; top: 64px;
    text-align: right; color: var(--ink);
    font-size: 15.5px; line-height: 23px;
  }
  .physician-name { color: var(--navy); font-weight: 700; }
  .header-divider {
    position: absolute; left: 610px; top: 58px;
    width: 1px; height: 116px; background: var(--rule);
  }
  .contact-list {
    position: absolute; left: 626px; top: 61px;
    list-style: none; color: var(--ink);
    font-size: 15.5px; line-height: 18px;
  }
  .contact-list li { display: flex; align-items: flex-start; margin-bottom: 6px; }
  .contact-icon { width: 17px; height: 17px; margin-right: 8px; flex: none; fill: var(--gold); }
  .header-rule {
    position: absolute; left: 47px; top: 203px;
    width: 778px; height: 1px; background: var(--rule);
  }
  .watermark {
    position: absolute; left: 207px; top: 382px;
    width: 436px; height: 436px;
    display: flex; align-items: center; justify-content: center;
    text-align: center;
    color: var(--watermark); font-weight: 700;
    font-size: 62px; line-height: 1.1;
  }
  .footer-band {
    position: absolute; left: 0; bottom: 0;
    width: 848px; height: 120px; display: block;
  }
</style>
</head>
<body>
  <main class="letterhead">
    <div class="brand-mark">RB Spine &amp; Vitality Center</div>

    <div class="physicians">
      <div class="physician-name">Lucinda Perrow, M.D.</div>
      <div class="physician-specialty">Hand and Upper Extremity Surgery</div>
      <div class="physician-name">Abena Quist, M.D.</div>
      <div class="physician-specialty">Hip &amp; Knee Replacement/General Orthopaedic Surgery</div>
    </div>

    <div class="header-divider"></div>

    <ul class="contact-list">
      <li>
        <svg class="contact-icon" viewBox="0 0 24 24"><path d="M6.6 10.8a15.1 15.1 0 0 0 6.6 6.6l2.2-2.2a1 1 0 0 1 1-.25 11.4 11.4 0 0 0 3.6.57 1 1 0 0 1 1 1V20a1 1 0 0 1-1 1A17 17 0 0 1 3 4a1 1 0 0 1 1-1h3.5a1 1 0 0 1 1 1c0 1.25.2 2.45.57 3.57a1 1 0 0 1-.25 1z"/></svg>
        954-218-4650
      </li>
      <li>
        <svg class="contact-icon" viewBox="0 0 24 24"><path d="M8 2h8v6H8zM3 7h4v15H3zM9 9h12v13H9zm2 3v2h2v-2zm4 0v2h2v-2zm-4 4v2h2v-2zm4 0v2h2v-2z"/></svg>
        954-582-1346
      </li>
      <li>
        <svg class="contact-icon" viewBox="0 0 24 24"><path d="M2 6h20v13H2zm2 2v.5l8 5 8-5V8l-8 5z"/></svg>
        info@myrbspine.com
      </li>
      <li>
        <svg class="contact-icon" viewBox="0 0 24 24"><path d="M12 2a7 7 0 0 0-7 7c0 5 7 13 7 13s7-8 7-13a7 7 0 0 0-7-7zm0 9.5A2.5 2.5 0 1 1 12 6.5a2.5 2.5 0 0 1 0 5z"/></svg>
        <span>18735 North Harlow Pkwy<br>Maple Grove, FL 33418</span>
      </li>
    </ul>

    <div class="header-rule"></div>

    <div class="watermark">RB Spine &amp; Vitality Center</div>

    <svg class="footer-band" viewBox="0 0 848 120" preserveAspectRatio="none" aria-hidden="true">
      <path fill="var(--navy)" d="M0 70 Q424 30 848 70 L848 120 L0 120 Z"/>
      <path fill="none" stroke="var(--gold)" stroke-width="4" d="M0 58 Q424 18 848 58"/>
    </svg>
  </main>
</body>
</html>
```